2018 Vision Board Workshop

I need to promote this workshop on both an 8.5x11 sheet and a 5x7 card. I do have a logo that needs to be present. I'd like to stay true to my branded colors. The flyer needs to project the excitement of a new year and the possibilities of what a person can create, produce, explore in their lives by putting it all on a vision board. Creating the vision of what you want will inspire you to achieve your goals and dreams. Looking at your vision board each day will propel you into taking action as you chart your course to achieve what you truly want.
The flyer needs to have the following information:
The workshop date and time - Sat., Jan. 13, 2018, 10:30-1:30
The location is - Atrium 47B, 2864 Birchwood Vale Rd, Colorado Springs, Co 80417
in the FORGE Room
My name and contact information - Mara Vollbeck
Text and voice 303-417-6652
Email - mara@brightwell-daily-craft.com
Website - brightwell-daily-craft.com
The fee is $45. All materials are provided.

My company is called Brightwell Daily Craft. I am a Life Coach, author, speaker and workshop leader.\ I wrote this program, Brightwell Daily Craft to teach concepts and supporting skills for living with more happiness, satisfaction and fulfillment. Thanks for reading this!! Mara

Target Market(s)

Primarily women, educated, motivated, proactive in their own lives and well being

Font styles to use
Other font styles liked:
• I have been using Century Gothic. I'm open to new ideas.

Requirements
Must have
• The Brightwell Daily Craft logo
• The flyer needs to have the following information:
• The workshop date and time - Sat., Jan. 13, 2018, 10:30-1:30
• The location is - Atrium 47B, 2864 Birchwood Vale Rd, Colorado Springs, Co 80417
• in the FORGE Room
• My name and contact information - Mara Vollbeck
• Text and voice 303-417-6652
• Email - mara@brightwell-daily-craft.com
• Website - brightwell-daily-craft.com
• The fee is $45. All materials are provided.
Nice to have
• The Brightwell Daily Craft branded colors in the design
• Images of vision boards

```html
<!DOCTYPE html>
<html lang="en">
<head>
<meta charset="utf-8">
<title>Get Happier in 2018 – Vision Board Workshop</title>
<link rel="stylesheet" href="https://fonts.googleapis.com/css2?family=Questrial&family=Didact+Gothic&display=swap">
<style>
  :root {
    --brand-blue: #1ea7ec;
    --brand-blue-light: #4dbcf2;
    --brand-green: #8fd400;
    --brand-green-text: #8cc63f;
    --ink: #222222;
    --paper: #ffffff;
    --stage: #eceef1;
    --photo-family-a: #c9b8a6;
    --photo-family-b: #e9e4dc;
    --photo-portrait-a: #d9a24a;
    --photo-portrait-b: #6fa8a0;
  }
  * { box-sizing: border-box; margin: 0; padding: 0; }
  html, body {
    width: 1200px; height: 861px; overflow: hidden;
    background: var(--stage);
    font-family: "Questrial", "Didact Gothic", sans-serif;
    color: var(--ink);
  }
  .stage {
    position: absolute; left: 0; top: 0;
    width: 1266px; height: 908px;
    transform: scale(0.9479);
    transform-origin: 0 0;
  }
  .piece {
    position: absolute; background: var(--paper); overflow: hidden;
    box-shadow: 0 2px 10px rgba(0,0,0,.15);
  }
  .piece > * { position: absolute; }
  .shapes { left: 0; top: 0; width: 100%; height: 100%; }
  .photo-family { background: linear-gradient(135deg, var(--photo-family-b) 0%, var(--photo-family-a) 55%, var(--photo-family-b) 100%); }
  .photo-portrait {
    background: linear-gradient(160deg, var(--photo-portrait-a) 0%, #e8c79a 50%, var(--photo-portrait-b) 100%);
    border: 2px solid #ffffff; outline: 1px solid #777;
  }
  .price-tag { color: #fff; text-align: center; line-height: 1.1; }
  .price-tag .amount { display: block; font-weight: 700; font-family: "Didact Gothic", sans-serif; }
  .brand { display: flex; align-items: center; color: var(--brand-green-text); white-space: nowrap; }
  .brand .dot { border-radius: 50%; background: var(--brand-green-text); display: inline-block; }
  .headline { color: var(--brand-blue-light); white-space: nowrap; letter-spacing: .5px;
    text-shadow: 0 0 1px var(--brand-blue); }
  .date-band { background: var(--brand-blue); color: #fff; white-space: nowrap; display: flex; align-items: center; }
  .date-band sup { font-size: .55em; }
  .room { text-transform: uppercase; white-space: nowrap; }
  .address, .contact { white-space: nowrap; line-height: 1.3; }
  .contact b { font-weight: 700; }
  .green-rule { background: var(--brand-green); }
  .leader-name { text-transform: uppercase; text-align: center; white-space: nowrap; }
  .leader-phone { text-align: center; white-space: nowrap; line-height: 1.25; }
  .leader-phone b { font-family: "Didact Gothic", sans-serif; font-weight: 700; }

  /* Letter flyer */
  .flyer { left: 93px; top: 66px; width: 558px; height: 756px; }
  .flyer .photo-family { left: 0; top: 0; width: 558px; height: 400px;
    clip-path: polygon(0 0, 100% 0, 100% 378px, 0 288px); }
  .flyer .price-tag { left: 401px; top: 0; width: 147px; height: 146px; padding-top: 20px; font-size: 19px; }
  .flyer .price-tag .amount { font-size: 48px; margin-bottom: 6px; }
  .flyer .brand { left: 25px; top: 385px; font-size: 29px; gap: 10px; }
  .flyer .brand .dot { width: 16px; height: 16px; }
  .flyer .headline { left: 22px; top: 452px; font-size: 44px; }
  .flyer .date-band { left: 0; top: 507px; width: 446px; height: 34px; padding-left: 30px; font-size: 23px; }
  .flyer .room { left: 91px; top: 616px; font-size: 18px; }
  .flyer .address { left: 28px; top: 641px; font-size: 18px; }
  .flyer .contact { left: 27px; top: 697px; font-size: 16.5px; }
  .flyer .green-rule { left: 27px; top: 746px; width: 284px; height: 10px; }
  .flyer .leader-name { left: 380px; top: 559px; width: 133px; font-size: 12.5px; }
  .flyer .photo-portrait { left: 382px; top: 578px; width: 129px; height: 133px; }
  .flyer .leader-phone { left: 370px; top: 716px; width: 153px; font-size: 14px; }

  /* 5x7 card */
  .card { left: 695px; top: 318px; width: 503px; height: 360px; }
  .card .photo-family { left: 0; top: 0; width: 503px; height: 230px;
    clip-path: polygon(0 0, 100% 0, 100% 222px, 0 136px); }
  .card .price-tag { left: 0; top: 0; width: 145px; height: 124px; padding-top: 14px; font-size: 15.5px; }
  .card .price-tag .amount { font-size: 40px; margin-bottom: 4px; }
  .card .brand { left: 30px; top: 195px; font-size: 14px; gap: 5px; }
  .card .brand .dot { width: 8px; height: 8px; }
  .card .headline { left: 12px; top: 221px; font-size: 22px; }
  .card .date-band { left: 12px; top: 251px; width: 254px; height: 17px; padding-left: 5px; font-size: 12px; }
  .card .room { left: 47px; top: 283px; font-size: 11.5px; }
  .card .address { left: 22px; top: 297px; font-size: 11px; }
  .card .contact { left: 21px; top: 324px; font-size: 9.5px; }
  .card .green-rule { left: 15px; top: 354px; width: 267px; height: 6px; }
  .card .leader-name { left: 350px; top: 246px; width: 76px; font-size: 7.5px; }
  .card .photo-portrait { left: 358px; top: 256px; width: 60px; height: 76px; }
  .card .leader-phone { left: 345px; top: 334px; width: 86px; font-size: 8.5px; }
</style>
</head>
<body>
<main class="stage">

  <article class="piece flyer">
    <div class="photo-family" role="img" aria-label="Photo of a smiling family of four seated together on a white sofa"></div>
    <svg class="shapes" viewBox="0 0 558 756" aria-hidden="true">
      <polygon points="0,288 558,378 558,396 507,434 0,300" fill="var(--brand-green)"/>
      <polygon points="507,434 558,396 558,566" fill="var(--brand-blue)"/>
      <polygon points="401,0 548,0 548,146 474,136 401,146" fill="var(--brand-blue)"/>
      <polyline points="410,128 474,120 540,128" fill="none" stroke="#fff" stroke-width="1.5"/>
      <polygon points="452,507 466,507 478,527 464,527" fill="var(--brand-green)"/>
      <polygon points="468,507 482,507 494,527 480,527" fill="var(--brand-green)"/>
      <g fill="none" stroke="#222" stroke-width="1.6">
        <path d="M145,598 c-8,-10 -14,-16 -14,-24 a14,14 0 0 1 28,0 c0,8 -6,14 -14,24 z"/>
        <circle cx="145" cy="574" r="5"/>
        <polyline points="136,594 128,606 162,606 154,594"/>
      </g>
    </svg>
    <div class="price-tag"><span class="amount">$45</span>ALL MATERIALS<br>ARE PROVIDED</div>
    <div class="brand"><span class="dot"></span>Brightwell Daily Craft</div>
    <h1 class="headline">GET HAPPIER IN 2018</h1>
    <p class="date-band">Saturday, 13<sup>th</sup>&nbsp;January 2018, 10:30-1:30</p>
    <p class="room">FORGE Room</p>
    <p class="address">Atrium 47B, 2864 Birchwood Vale Rd,<br>Colorado Springs, Co 80417</p>
    <p class="contact">Email - mara@brightwell-daily-craft.com<br>Website - <b>brightwell-daily-craft</b>.com</p>
    <div class="green-rule"></div>
    <p class="leader-name">Mara Vollbeck</p>
    <div class="photo-portrait" role="img" aria-label="Portrait photo of the workshop leader outdoors"></div>
    <p class="leader-phone">Text and voice<br><b>303-417-6652</b></p>
  </article>

  <article class="piece card">
    <div class="photo-family" role="img" aria-label="Photo of a smiling family of four seated together on a white sofa"></div>
    <svg class="shapes" viewBox="0 0 503 360" aria-hidden="true">
      <polygon points="0,136 503,222 503,226 466,238 0,147" fill="var(--brand-green)"/>
      <polygon points="466,238 503,226 503,360 492,360" fill="var(--brand-blue)"/>
      <polygon points="0,0 145,0 145,124 72,116 0,124" fill="var(--brand-blue)"/>
      <polyline points="6,110 72,103 139,110" fill="none" stroke="#fff" stroke-width="1.2"/>
      <polygon points="256,251 265,251 273,264 264,264" fill="var(--brand-green)"/>
      <polygon points="267,251 276,251 284,264 275,264" fill="var(--brand-green)"/>
      <g fill="none" stroke="#222" stroke-width="1.1">
        <path d="M34,294 c-5,-6 -8,-9 -8,-14 a8,8 0 0 1 16,0 c0,5 -3,8 -8,14 z"/>
        <circle cx="34" cy="280" r="3"/>
      </g>
    </svg>
    <div class="price-tag"><span class="amount">$45</span>ALL MATERIALS<br>ARE PROVIDED</div>
    <div class="brand"><span class="dot"></span>Brightwell Daily Craft</div>
    <h2 class="headline">GET HAPPIER IN 2018</h2>
    <p class="date-band">Saturday, 13<sup>th</sup>&nbsp;January 2018, 10:30-1:30</p>
    <p class="room">FORGE Room</p>
    <p class="address">Atrium 47B, 2864 Birchwood Vale Rd,<br>Colorado Springs, Co 80417</p>
    <p class="contact">Email - mara@brightwell-daily-craft.com<br>Website - <b>brightwell-daily-craft</b>.com</p>
    <div class="green-rule"></div>
    <p class="leader-name">Mara Vollbeck</p>
    <div class="photo-portrait" role="img" aria-label="Portrait photo of the workshop leader outdoors"></div>
    <p class="leader-phone">Text and voice<br><b>303-417-6652</b></p>
  </article>

</main>
</body>
</html>
```